Owen Tasker Studios Business Card

Looking for a clear, modern, elegant, sharp business card that conveys a professional yet edgy image to my business as a wedding, portrait, and travel photographer. Would like something that looks vintage yet modern. Need a new business card to grow my business. We are growing the business for Wedding and Event Photography as well as fine art Photography. (Mostly Landscapes)
Updates

I’m looking through designs now but I have a new logo that i want using please.

New logo uploaded please redesign using that

PLEASE ALL DESIGNERS LOOK IN BRIEF FOR NEW LOGO

Target Market(s)

Brides, Grooms, Families with Kids, People looking for Fine Art Photography Artwork

Industry/Entity Type

Photographer

Contact Information for Business Card

Unsure

Font styles to use
Serif

Colors

Designer to choose colors to be used in the design.

Requirements
Must have
• My Website:
• http://taskerlens.examplefolio.net
• Phone:
• 323-481-5206
• Email:
• owentaskerlens@mailbox-example.net
Nice to have
• Would like a sort of shine on the printing finish.
• I like black I think it looks good on a business card.
• Can try working with my logo (png that I've attached)

```html
<!DOCTYPE html>
<html lang="en">
<head>
<meta charset="utf-8">
<title>Owen Tasker Studios Business Card</title>
<link href="https://fonts.googleapis.com/css2?family=Bitter:wght@700&family=Lato:wght@300;400&display=swap" rel="stylesheet">
<style>
  :root {
    --backdrop: #e0e0e0;
    --paper: #efede0;
    --ink: #2a2a2a;
    --ink-soft: #444444;
    --charcoal: #333333;
    --emboss: #1e1e1e;
  }
  html, body {
    margin: 0;
    padding: 0;
    width: 1200px;
    height: 897px;
    overflow: hidden;
    background: var(--backdrop);
  }
  .canvas {
    position: relative;
    width: 1200px;
    height: 897px;
  }
  .card {
    position: absolute;
    left: 303px;
    width: 595px;
    height: 338px;
    overflow: hidden;
  }
  .card-front {
    top: 92px;
    background: var(--paper);
  }
  .card-back {
    top: 469px;
    background: var(--charcoal);
  }
  .owner-name {
    position: absolute;
    left: 31px;
    top: 30px;
    margin: 0;
    font-family: "Bitter", serif;
    font-weight: 700;
    font-size: 21px;
    letter-spacing: 0.04em;
    color: var(--ink);
  }
  .owner-role {
    position: absolute;
    left: 31px;
    top: 56px;
    margin: 0;
    font-family: "Lato", sans-serif;
    font-size: 14.5px;
    color: var(--ink-soft);
  }
  .contact-list {
    position: absolute;
    left: 31px;
    top: 272px;
    margin: 0;
    padding: 0;
    list-style: none;
    font-family: "Lato", sans-serif;
    font-size: 14px;
    color: var(--ink-soft);
  }
  .contact-list li {
    display: flex;
    align-items: center;
    height: 19px;
  }
  .contact-icon {
    width: 10px;
    height: 10px;
    margin-right: 8px;
    fill: none;
    stroke: var(--ink);
    stroke-width: 1.4;
  }
  .website {
    position: absolute;
    right: 33px;
    top: 291px;
    margin: 0;
    font-family: "Lato", sans-serif;
    font-size: 14px;
    color: var(--ink-soft);
  }
  .accent-bar {
    position: absolute;
    left: 327px;
    width: 235px;
    top: 330px;
    height: 8px;
    background: var(--charcoal);
  }
  .brand-square {
    position: absolute;
    left: 260px;
    top: 94px;
    width: 72px;
    height: 72px;
    border: 1.5px solid var(--emboss);
    box-sizing: border-box;
  }
  .brand-name {
    position: absolute;
    left: 0;
    right: 0;
    top: 182px;
    margin: 0;
    text-align: center;
    font-family: "Lato", sans-serif;
    font-weight: 300;
    color: var(--emboss);
  }
  .brand-name .line-main {
    display: block;
    font-size: 34px;
    line-height: 40px;
  }
  .brand-name .line-sub {
    display: block;
    font-size: 13px;
    letter-spacing: 0.62em;
    margin-left: 0.62em;
    line-height: 22px;
  }
</style>
</head>
<body>
<main class="canvas">
  <section class="card card-front">
    <h1 class="owner-name">OWEN TASKER</h1>
    <p class="owner-role">Photographer</p>
    <ul class="contact-list">
      <li>
        <svg class="contact-icon" viewBox="0 0 10 10" aria-hidden="true"><path d="M2 1 L3.5 1 L4 3 L3 4 Q4 6.5 6 7 L7 6 L9 6.5 L9 8 Q5 9.5 1.5 4.5 Q1 2.5 2 1 Z"/></svg>
        323-481-5206
      </li>
      <li>
        <svg class="contact-icon" viewBox="0 0 10 10" aria-hidden="true"><rect x="0.8" y="2" width="8.4" height="6"/><path d="M0.8 2 L5 5.5 L9.2 2"/></svg>
        owentaskerlens@mailbox-example.net
      </li>
    </ul>
    <p class="website">www.taskerlens.examplefolio.net</p>
    <div class="accent-bar"></div>
  </section>

  <section class="card card-back">
    <div class="brand-square"></div>
    <h2 class="brand-name">
      <span class="line-main">OWEN TASKER</span>
      <span class="line-sub">STUDIOS</span>
    </h2>
  </section>
</main>
</body>
</html>
```